buseisness card

design a card that similar to my web site
BRIXENTAPLORLLC .COM

Contact Information for Business Card

NAME PHONE # WEBSITE EMAIL AND DISCTIPTION OF WHAT WE DO

Colors
0054AA
0677BA
7BADD7
CADEEF
E8F1F8

Requirements
Must have
• lOGO AND DETAILS
Nice to have
• I LIKE THE WATER LIKE ON MY WEB SITE

```html
<!DOCTYPE html>
<html lang="en">
<head>
<meta charset="utf-8">
<title>Brixen Taplor – Business Card</title>
<link href="https://fonts.googleapis.com/css2?family=Montserrat:wght@700&family=Arimo:wght@400&display=swap" rel="stylesheet">
<style>
  :root {
    --brand-blue: #1981b4;
    --mist: #dce9f3;
    --paper: #ffffff;
    --frame: #222222;
  }
  html, body {
    margin: 0;
    padding: 0;
    width: 1200px;
    height: 1001px;
    overflow: hidden;
    background: var(--paper);
  }
  .sheet {
    position: relative;
    width: 1200px;
    height: 1001px;
    box-sizing: border-box;
    border: 2px solid var(--frame);
    background: var(--paper);
  }
  .card {
    position: absolute;
    left: 259px;
    width: 683px;
    height: 417px;
    overflow: hidden;
  }
  .card--front { top: 70px; background: var(--paper); }
  .card--back  { top: 513px; background: var(--brand-blue); }

  .watermark-area {
    position: absolute;
    left: 130px;
    top: 0;
    width: 300px;
    height: 417px;
    background: radial-gradient(ellipse at 60% 55%, var(--mist) 0%, rgba(220,233,243,0.5) 45%, rgba(255,255,255,0) 75%);
  }
  .feature-panel {
    position: absolute;
    left: 414px;
    top: 0;
    width: 269px;
    height: 417px;
    background: var(--brand-blue);
  }

  .brand {
    position: absolute;
    text-align: center;
    font-family: "Montserrat", sans-serif;
    font-weight: 700;
    font-size: 27px;
    letter-spacing: 0.3px;
    white-space: nowrap;
  }
  .brand-dot {
    display: block;
    margin: 0 auto 14px;
    width: 80px;
    height: 80px;
    border-radius: 50%;
  }
  .brand--front { left: 48px; top: 30px; width: 270px; color: var(--brand-blue); }
  .brand--front .brand-dot { background: var(--brand-blue); }
  .brand--back { left: 0; top: 165px; width: 683px; color: var(--paper); }
  .brand--back .brand-dot { background: var(--paper); }

  .contact-list {
    position: absolute;
    left: 38px;
    top: 226px;
    margin: 0;
    padding: 0;
    list-style: none;
    font-family: "Arimo", sans-serif;
    font-size: 16px;
    line-height: 18px;
    color: var(--brand-blue);
  }
  .contact-item {
    position: relative;
    padding-left: 45px;
    margin-bottom: 13px;
  }
  .contact-item svg {
    position: absolute;
    left: 0;
    top: -2px;
    width: 22px;
    height: 22px;
    fill: none;
    stroke: var(--brand-blue);
    stroke-width: 1.5;
  }

  .feature-list {
    position: absolute;
    left: 459px;
    top: 137px;
    margin: 0;
    padding: 0;
    list-style: none;
    font-family: "Arimo", sans-serif;
    font-size: 16px;
    color: var(--paper);
  }
  .feature-item {
    position: relative;
    padding-left: 25px;
    height: 31px;
    line-height: 18px;
  }
  .feature-item svg {
    position: absolute;
    left: 0;
    top: 0;
    width: 16px;
    height: 16px;
    fill: none;
    stroke: var(--paper);
    stroke-width: 1.5;
  }
</style>
</head>
<body>
<div class="sheet">

  <section class="card card--front">
    <div class="watermark-area" role="img" aria-label="Faint soft-blue water background decoration"></div>
    <div class="feature-panel"></div>

    <div class="brand brand--front">
      <span class="brand-dot"></span>
      BRIXEN TAPLOR
    </div>

    <ul class="contact-list">
      <li class="contact-item">
        <svg viewBox="0 0 24 24"><rect x="2" y="5" width="20" height="14" rx="2"/><path d="M2 6l10 7 10-7"/></svg>
        hello@bt482.com
      </li>
      <li class="contact-item">
        <svg viewBox="0 0 24 24"><path d="M5 3l4 1 1 4-2 2a12 12 0 0 0 6 6l2-2 4 1 1 4-3 2C10 20 4 14 3 6z"/><path d="M15 3a6 6 0 0 1 6 6M15 7a2 2 0 0 1 2 2"/></svg>
        +740 555 0182
      </li>
      <li class="contact-item">
        <svg viewBox="0 0 24 24"><circle cx="12" cy="12" r="10"/><ellipse cx="12" cy="12" rx="4" ry="10"/><path d="M2 12h20M4 7h16M4 17h16"/></svg>
        brixentaplorllc.com
      </li>
      <li class="contact-item">
        <svg viewBox="0 0 24 24"><path d="M12 22s7-7 7-12a7 7 0 0 0-14 0c0 5 7 12 7 12z"/><circle cx="12" cy="10" r="2.5"/></svg>
        1840 Meridian<br>Parkway<br>Columbus, OH 43215
      </li>
    </ul>

    <ul class="feature-list">
      <li class="feature-item"><svg viewBox="0 0 16 16"><rect x="1" y="2" width="13" height="13"/><path d="M4 8l3 3 8-10"/></svg>Professional Staff</li>
      <li class="feature-item"><svg viewBox="0 0 16 16"><rect x="1" y="2" width="13" height="13"/><path d="M4 8l3 3 8-10"/></svg>Cost Effective</li>
      <li class="feature-item"><svg viewBox="0 0 16 16"><rect x="1" y="2" width="13" height="13"/><path d="M4 8l3 3 8-10"/></svg>Variable Effective</li>
      <li class="feature-item"><svg viewBox="0 0 16 16"><rect x="1" y="2" width="13" height="13"/><path d="M4 8l3 3 8-10"/></svg>Environment Friendly</li>
      <li class="feature-item"><svg viewBox="0 0 16 16"><rect x="1" y="2" width="13" height="13"/><path d="M4 8l3 3 8-10"/></svg>Thorough Testing</li>
    </ul>
  </section>

  <section class="card card--back">
    <div class="brand brand--back">
      <span class="brand-dot"></span>
      BRIXEN TAPLOR
    </div>
  </section>

</div>
</body>
</html>
```